Simple Modern Label for a Coconut oil product

We need a label designed for Organic Coconut oil. We would like the label to convey the gourmet/high quality product. It should be modern and simple and look like an artisinal product. The label will need to contain all the basic label requirements - Independence list, place for nutrition facts, our company logo etc.
The label will ultimately be printed as oil proof, so it will have a glossy appearance.
I have includes some examples that I like and a file with the logo.

Product Container - Wide Mount Clear Glass Jar: 4.75 inches tall (base to the bottom of the lid) and 9.5 in circumference
Label: Can be 1 or 2 separate labels, round, square and rectangle are okay
No larger than 3 inches high and 9 inches long

Target Market(s)

Middle Age home chef

Industry/Entity Type

Product

Requirements
Must have
• - logo (Attached below, I have this in multiple formats, let me know if you need them)
• - 14 FL OZ (414mL)
• - ingredient: organic unrefined whole kernel virgin coconut oil,
• - Manufacturer: XXX Y St., anywhere, CA, 99999
• - Distributed by Fernvale Naturals, P.O. Box 5521, Oakland, CA 94610 www.FernvaleNaturals.example
• - Certified Organic by Company Name
• - Product of Sri Lanka
Nice to have
• - Nutrition Facts
Should not have
• Clutter

```html
<!DOCTYPE html>
<html lang="en">
<head>
<meta charset="utf-8">
<title>Fernvale Naturals – Organic Virgin Coconut Oil Label</title>
<link href="https://fonts.googleapis.com/css2?family=Quicksand:wght@300;500&display=swap" rel="stylesheet">
<style>
  :root {
    --page-bg: #f4f4ef;
    --label-dark: #3a3a3a;
    --label-mid: #474747;
    --drop-white: #ffffff;
    --ink-light: #ececec;
    --ink-soft: #bdbdbd;
    --rule: #9a9a9a;
  }
  html, body {
    margin: 0;
    width: 1200px;
    height: 1200px;
    overflow: hidden;
    background: var(--page-bg);
  }
  .canvas {
    position: relative;
    width: 1200px;
    height: 1200px;
  }
  .label {
    position: absolute;
    left: 170px;
    top: 270px;
    width: 860px;
    height: 660px;
    background: linear-gradient(90deg, var(--label-dark) 0%, var(--label-mid) 50%, var(--label-dark) 100%);
    color: var(--ink-light);
    font-family: "Quicksand", sans-serif;
    text-align: center;
  }
  .label__drop {
    position: absolute;
    left: 0;
    top: 0;
  }
  .brand {
    position: absolute;
    left: 0;
    right: 0;
    top: 330px;
    margin: 0;
    font-weight: 500;
    font-size: 40px;
    letter-spacing: 3px;
    line-height: 1;
    text-transform: uppercase;
  }
  .brand__rule {
    position: absolute;
    left: 260px;
    width: 340px;
    top: 390px;
    height: 1px;
    background: var(--rule);
  }
  .product-name {
    position: absolute;
    left: 0;
    right: 0;
    top: 406px;
    margin: 0;
    font-weight: 300;
    font-size: 46px;
    line-height: 44px;
    letter-spacing: 1px;
  }
  .net-volume {
    position: absolute;
    left: 0;
    right: 0;
    top: 512px;
    margin: 0;
    font-weight: 500;
    font-size: 22px;
    line-height: 1;
    letter-spacing: 3px;
  }
  .fine-print {
    position: absolute;
    left: 40px;
    right: 40px;
    top: 560px;
    margin: 0;
    font-weight: 500;
    font-size: 13px;
    line-height: 19px;
    letter-spacing: 0.5px;
    color: var(--ink-soft);
  }
  .fine-print p {
    margin: 0;
  }
</style>
</head>
<body>
<main class="canvas">
  <section class="label">
    <svg class="label__drop" width="860" height="320" viewBox="0 0 860 320" aria-hidden="true">
      <path d="M410 0 L450 0 C450 70 530 110 530 210 A100 100 0 0 1 330 210 C330 110 410 70 410 0 Z" fill="var(--drop-white)"/>
    </svg>
    <h1 class="brand">Fernvale Naturals</h1>
    <div class="brand__rule"></div>
    <p class="product-name">organic virgin<br>coconut oil</p>
    <p class="net-volume">14 FL . OZ (414mL)</p>
    <div class="fine-print">
      <p>Ingredients: organic unrefined whole kernel virgin coconut oil.</p>
      <p>Manufacturer: XXX Y St., Anywhere, CA 99999 · Product of Sri Lanka</p>
      <p>Distributed by Fernvale Naturals, P.O. Box 5521, Oakland, CA 94610 · www.FernvaleNaturals.example</p>
      <p>Certified Organic by Company Name</p>
    </div>
  </section>
</main>
</body>
</html>
```